Tallyden Web Design

Create Website Design for Tallyden. Tallyden is online application for collaboration team work system (task list management). More concept design for this project please find attach file ("tallyden website concept.pdf") . But my concept is just describe minimal features not bind design

For tallyden logo, i had already attach files. But i had not decided what color i chose, so it's okay if you suggest logo color for your suitable website design.
Updates

Dear All Designer,

I like brisk carousel (http://quillforge-labs.example/brisk-carousel/),
may be your concept design can adjust with this concept.
but don't worry about script for brisk carousel, my team will be handle
You just make website design to suitable with brisk carousel

but if you had own website design concept are welcome

thanks

Target Market(s)

Business Company

Industry/Entity Type

Management

```html
<!DOCTYPE html>
<html lang="en">
<head>
<meta charset="utf-8">
<title>Tallyden – Online Collaboration Team Work</title>
<link rel="stylesheet" href="https://fonts.googleapis.com/css2?family=Arimo:wght@400;700&family=Lato:wght@400;700&display=swap">
<style>
:root{
  --green:#7aa832;
  --green-light:#a6cc5a;
  --green-pale:#c9e38e;
  --lime:#8cc63f;
  --lime-bright:#b6e04a;
  --teal:#1f5e68;
  --teal-dark:#163f48;
  --ink:#1d4a5a;
  --nav:#2b4a16;
  --white:#ffffff;
  --card:#f6fbe6;
  --body:#4a4a4a;
  --link:#1a6a9a;
  --footer-text:#e6f3c8;
  --rule:rgba(255,255,255,.25);
}
*{box-sizing:border-box;margin:0;padding:0}
html,body{width:1140px;height:1200px;overflow:hidden}
body{
  position:relative;
  font-family:"Lato",sans-serif;
  background:
    radial-gradient(ellipse 520px 90px at 570px 60px,rgba(255,255,255,.25),transparent 70%),
    radial-gradient(ellipse 560px 50px at 570px 523px,rgba(255,255,255,.35),transparent 70%),
    linear-gradient(var(--green),#79a631 60%,#73a02d);
}
.abs{position:absolute}

/* header */
.brand{left:165px;top:22px;display:flex;align-items:center;gap:10px;
  font-family:"Arimo",sans-serif;font-weight:700;font-size:50px;color:var(--teal);letter-spacing:-1px}
.brand-dot{width:22px;height:22px;border-radius:50%;background:var(--lime-bright)}
.main-nav{left:532px;top:53px;display:flex;font-family:"Arimo",sans-serif;font-size:11px;white-space:nowrap}
.main-nav a{color:var(--white);text-decoration:none;padding:0 8px;border-left:1px dotted rgba(255,255,255,.6)}
.main-nav a:first-child{color:var(--nav);border:none;padding-left:0}
.btn-login,.btn-signup{top:49px;height:23px;font-family:"Arimo",sans-serif;font-weight:700;font-size:11px;
  color:var(--white);display:flex;align-items:center;justify-content:center;border:1px solid rgba(255,255,255,.7)}
.btn-login{left:884px;width:60px;background:linear-gradient(#c4ea5a,#8cc63f)}
.btn-signup{left:952px;width:61px;background:linear-gradient(#3a8aa0,#1f5e68)}
.header-rule{left:140px;top:104px;width:860px;height:1px;background:rgba(255,255,255,.3)}

/* hero */
.hero-visual{left:150px;top:128px;width:390px;height:300px;border-radius:10px;
  background:radial-gradient(ellipse at 50% 45%,#e9eef2,#9aa6ad 60%,rgba(122,168,50,0) 75%)}
.hero-title{left:565px;top:138px;width:500px;font-family:"Arimo",sans-serif;font-weight:700;font-size:35px;
  line-height:43px;color:var(--white);text-shadow:0 2px 3px rgba(0,0,0,.35);white-space:nowrap}
.hero-text{left:565px;top:238px;width:410px;font-size:11.5px;line-height:16px;color:var(--white)}
.hero-arrow{left:900px;top:210px}
.cta{left:566px;top:291px;width:333px;height:64px;border-radius:4px;
  background:linear-gradient(#2b7785,#174e58);border:1px solid rgba(255,255,255,.35);
  box-shadow:0 3px 6px rgba(0,0,0,.3);
  font-family:"Arimo",sans-serif;font-weight:700;font-size:19px;line-height:24px;color:var(--lime-bright);
  display:flex;align-items:center;justify-content:center;text-align:center}
.cta::before{content:"";position:absolute;left:176px;top:-8px;border:8px solid transparent;border-top:0;border-bottom-color:#2b7785}

/* section banner */
.section-band{left:140px;top:487px;width:860px;height:72px;
  border-top:1px solid var(--rule);border-bottom:1px solid var(--rule);
  background:radial-gradient(ellipse at 50% 50%,rgba(215,240,140,.55),rgba(215,240,140,0) 70%)}
.section-title{left:140px;top:503px;width:860px;text-align:center;font-family:"Arimo",sans-serif;font-weight:700;
  font-size:30px;line-height:38px;color:var(--white);text-shadow:0 2px 3px rgba(0,0,0,.3);white-space:nowrap}

/* feature cards */
.card{top:602px;width:275px;height:272px;background:linear-gradient(#ffffff,var(--card) 60%,#e7f3c4);
  border:1px solid #dcebb0;box-shadow:0 2px 4px rgba(0,0,0,.15);text-align:center}
.card-title{margin-top:30px;font-family:"Arimo",sans-serif;font-weight:700;font-size:19px;color:var(--ink);white-space:nowrap}
.card-title span{color:var(--lime)}
.card-art{margin:10px auto 0;width:210px;height:135px;border-radius:8px}
.art-apps{background:radial-gradient(ellipse at 50% 50%,#f2f2f2,#d7dce0 50%,rgba(255,255,255,0) 72%)}
.art-sync{background:radial-gradient(ellipse at 50% 50%,#bfe2f5,#8a9aa4 45%,rgba(255,255,255,0) 72%)}
.art-report{background:radial-gradient(ellipse at 50% 50%,#eef2f5,#9aa3a9 55%,rgba(255,255,255,0) 75%)}
.card-text{margin:18px auto 0;width:240px;font-size:11.5px;line-height:16px;color:var(--body)}
.card-more{display:inline-block;margin-top:5px;font-family:"Arimo",sans-serif;font-weight:700;font-size:8.5px;color:var(--link);text-decoration:none}

/* footer */
.footer-col{top:975px;font-family:"Arimo",sans-serif}
.footer-col h3{font-weight:400;font-size:15px;color:var(--white);margin-bottom:12px}
.footer-col ul{list-style:none}
.footer-col li{height:29px;line-height:18px;font-size:11px;color:var(--footer-text);
  border-bottom:1px solid rgba(255,255,255,.18);width:150px;padding-top:4px;white-space:nowrap}
.footer-col li:last-child{border-bottom:none}
.social li{display:flex;align-items:center;gap:20px;margin-left:-14px;padding-left:6px}
.social i{width:17px;height:17px;border-radius:3px;display:block}
.i-a{background:#3b5b99}.i-b{background:#3fb0e0}.i-c{background:#cf3a2a}.i-d{background:#f07a1a}
.contact-form{left:783px;top:1012px;width:202px}
.field{background:linear-gradient(#ffffff,#f0f0f0);border:1px solid #d8e8b8;font-size:11px;color:#777;
  padding:8px 9px;position:absolute;white-space:nowrap}
.f-name{left:0;top:0;width:96px;height:28px}
.f-mail{left:106px;top:0;width:96px;height:28px}
.f-msg{left:0;top:37px;width:202px;height:50px}
.submit{position:absolute;left:1px;top:98px;width:102px;height:24px;border:1px solid rgba(255,255,255,.7);
  background:linear-gradient(#c4ea5a,#8cc63f);color:var(--white);font-family:"Arimo",sans-serif;font-weight:700;font-size:11px;
  display:flex;align-items:center;justify-content:center}
.footer-band{left:0;top:1158px;width:1140px;height:42px;
  background:radial-gradient(ellipse 500px 40px at 570px 21px,rgba(80,120,30,.35),transparent 75%)}
.copyright{left:0;top:1173px;width:1140px;text-align:center;font-family:"Arimo",sans-serif;font-size:9.5px;color:var(--footer-text)}
</style>
</head>
<body>

<header>
  <div class="abs brand">tallyden<span class="brand-dot"></span></div>
  <nav class="abs main-nav">
    <a>Home</a><a>Pricing</a><a>Features</a><a>Support</a><a>About us</a><a>Contact us</a>
  </nav>
  <a class="abs btn-login">LOGIN</a>
  <a class="abs btn-signup">SIGNUP</a>
  <div class="abs header-rule"></div>
</header>

<section class="hero">
  <div class="abs hero-visual" role="img" aria-label="Laptop showing the Tallyden dashboard with a play button, surrounded by round portraits of three team members joined by dashed arrows"></div>
  <h1 class="abs hero-title">Customize Online<br>Collaboration Team Work</h1>
  <p class="abs hero-text">Lorem ipsum dolor sit amet. Sed do eiusmod tempor incididunt ut labor. Lorem ipsum dolor sit amet. Sed do eiusmod tempor incididunt ut labor</p>
  <svg class="abs hero-arrow" width="110" height="130" viewBox="0 0 110 130" aria-hidden="true">
    <path d="M92 10 Q104 90 16 117" fill="none" stroke="#fff" stroke-width="2" stroke-dasharray="5 4"/>
    <path d="M14 117 l10 -6 l-2 12 z" fill="#fff"/>
  </svg>
  <a class="abs cta">Get started with a free<br>version of Tallyden copy Now!</a>
</section>

<section class="features">
  <div class="abs section-band"></div>
  <h2 class="abs section-title">Online Application For Collaboration Team Work System</h2>

  <article class="abs card" style="left:140px">
    <h3 class="card-title">Customize <span>Application</span></h3>
    <div class="card-art art-apps" role="img" aria-label="Open white box filled with colourful application icons"></div>
    <p class="card-text">Lorem ipsum dolor sit amet. Sed do eiusmod tempor incididunt ut labor</p>
    <a class="card-more">READ MORE &raquo;</a>
  </article>

  <article class="abs card" style="left:438px">
    <h3 class="card-title">Synchronize <span>All Device</span></h3>
    <div class="card-art art-sync" role="img" aria-label="Blue cloud connected to a laptop, phone and tablet"></div>
    <p class="card-text">Lorem ipsum dolor sit amet. Sed do eiusmod tempor incididunt ut labor</p>
    <a class="card-more">READ MORE &raquo;</a>
  </article>

  <article class="abs card" style="left:732px">
    <h3 class="card-title">Report</h3>
    <div class="card-art art-report" role="img" aria-label="Laptop displaying report bar and pie charts"></div>
    <p class="card-text">Lorem ipsum dolor sit amet. Sed do eiusmod tempor incididunt ut labor</p>
    <a class="card-more">READ MORE &raquo;</a>
  </article>
</section>

<footer>
  <div class="abs footer-col" style="left:176px">
    <h3>Navigations</h3>
    <ul><li>Home</li><li>Pricing</li><li>Features</li><li>Support</li><li>Contact Us</li></ul>
  </div>
  <div class="abs footer-col" style="left:388px">
    <h3>Links</h3>
    <ul><li>FAQ</li><li>Terms &amp; Conditions</li><li>Privacy Policy</li><li>Customers</li><li>Disclamer</li></ul>
  </div>
  <div class="abs footer-col social" style="left:595px">
    <h3>Social</h3>
    <ul>
      <li><i class="i-a"></i>Friendwall</li>
      <li><i class="i-b"></i>Chirpline</li>
      <li><i class="i-c"></i>Searchly</li>
      <li><i class="i-d"></i>RSS</li>
    </ul>
  </div>
  <div class="abs footer-col" style="left:783px">
    <h3>Contact Us</h3>
  </div>
  <form class="abs contact-form">
    <div class="field f-name">Your Name</div>
    <div class="field f-mail">Your email</div>
    <div class="field f-msg">Enter your Message</div>
    <div class="submit">SUBMIT NOW!</div>
  </form>
  <div class="abs footer-band"></div>
  <p class="abs copyright">Copyright © 2013 tallyden.example All rights reserved.</p>
</footer>

</body>
</html>
```